SEO wiki for a know-how website (rankvale.ch)

Hi,

i need a know-how wiki for an SEO website that looks similar to:

http://demo.plumtorx.com/#knowhow

With following know-how categories instead of "account settings" and "API questions":
- Content SEO
- Technical SEO
- Link building
- Influencer marketing
- paid marketing
- analytics & measurement

So i Need the following pages:
1. Landing page with the categories, the search bar and the side-bar
- Sidebar has latest articles, popular articles and categories (in this order)
- On top a nice logo
- on top right -> blog, contact
- on top right below -> social media buttons: corvaline, chirpnest

2. a blog site with
- headline
- sub-headline
- date, name
- rating with 5 "know-how" stars
- picture
- article
- info about the author
- related articles
- integration of comment plugin VORBLE

Target Market(s)

SEO folks

Industry/Entity Type

Seo

Logo Text

Own-hands tuning SEO

Number of Pages Required

2 page

Font styles to use
Sans Serif

Colors

Designer to choose colors to be used in the design.

```html
<!DOCTYPE html>
<html lang="en">
<head>
<meta charset="utf-8">
<title>skillnook – Knowledge Base</title>
<link href="https://fonts.googleapis.com/css2?family=Open+Sans:wght@400;600;700&family=Arimo&display=swap" rel="stylesheet">
<style>
:root{
  --blue:#0585ab;
  --blue-deep:#0a7ea3;
  --header:#3c3c3c;
  --page:#e6e6e6;
  --white:#ffffff;
  --ink:#333333;
  --muted:#555555;
  --icon:#2c3e50;
  --card-line:#dcdcdc;
  --card-tint:#f4f4f4;
  --rule:#dddddd;
}
*{box-sizing:border-box;margin:0;padding:0}
html,body{width:1102px;height:1200px;overflow:hidden;background:var(--page)}
body{font-family:"Open Sans",sans-serif;color:var(--ink)}
.stage{position:relative;width:1300px;height:1416px;transform:scale(0.84769);transform-origin:0 0;background:var(--page)}

/* header */
.site-header{position:absolute;left:0;top:0;width:1300px;height:78px;background:var(--header)}
.brand{position:absolute;left:143px;top:16px;display:flex;align-items:center;gap:8px;color:var(--white)}
.brand-dot{width:42px;height:42px;border-radius:50%;background:#3fc6d8}
.brand-name{font-size:29px;font-weight:600;line-height:28px}
.brand-tag{font-size:12px;line-height:14px}
.nav{position:absolute;top:23px;left:0;width:1300px;height:32px;font-size:14px}
.nav a{position:absolute;top:0;line-height:32px;color:var(--white);text-decoration:none}
.nav .active{left:790px;width:77px;text-align:center;background:var(--blue-deep);border-radius:16px}

/* search band */
.search-band{position:absolute;left:0;top:78px;width:1300px;height:150px;background:var(--blue)}
.search-box{position:absolute;left:143px;top:46px;width:999px;height:62px;border:1px solid rgba(255,255,255,.25);border-radius:31px}
.search-text{position:absolute;left:25px;top:20px;font-family:Arimo,sans-serif;font-size:16px;color:var(--white)}
.search-btn{position:absolute;left:857px;top:12px;width:116px;height:39px;border-radius:20px;background:var(--white);color:var(--blue);font-size:15px;display:flex;align-items:center;justify-content:center;gap:6px}

/* content */
.content{position:absolute;left:100px;top:228px;width:1100px;height:1062px;background:var(--white)}
.section-title{position:absolute;left:139px;top:272px;font-size:24px;font-weight:600;color:var(--ink);padding-left:21px;line-height:30px}
.section-title::before{content:"";position:absolute;left:0;top:5px;width:10px;height:22px;background:var(--blue)}
.section-title .lead{color:var(--blue);font-weight:400}

.card{position:absolute;width:309px;height:245px;border:1px solid var(--card-line);background:var(--white)}
.card.tinted{background:var(--card-tint)}
.card-icon{position:absolute;left:-13px;top:-11px;width:56px;height:56px;border-radius:50%;border:1px solid var(--card-line);background:var(--white)}
.card-icon.filled{background:var(--blue);border-color:var(--blue)}
.card-icon svg{position:absolute;left:0;top:0}
.card-title{position:absolute;left:60px;top:7px;font-size:19px;font-weight:400;color:var(--ink)}
.card.tinted .card-title{color:var(--blue)}
.card ul{position:absolute;left:14px;top:61px;list-style:none}
.card li{height:33px;font-size:14.5px;color:var(--muted);padding-left:29px;position:relative;line-height:22px}
.card li svg{position:absolute;left:0;top:3px}
.card li.no-tick svg{display:none}
.divider{position:absolute;left:134px;width:703px;border-top:1px dashed #cccccc}

/* sidebar */
.widget-head{position:absolute;left:888px;width:283px;height:36px;background:var(--blue);color:var(--white);font-size:16px;font-weight:400;line-height:36px;padding-left:41px}
.widget-head svg{position:absolute;left:11px;top:8px}
.widget-head::after{content:"";position:absolute;left:133px;bottom:-8px;border-left:8px solid transparent;border-right:8px solid transparent;border-top:8px solid var(--blue)}
.side-list{position:absolute;left:894px;width:268px;list-style:none;font-size:13px;color:var(--ink);line-height:20px}
.side-list li{position:relative;padding-left:40px}
.side-list svg{position:absolute;left:0;top:2px}
.count{position:absolute;right:0;top:0;color:var(--blue);font-weight:700}
.side-rule{position:absolute;left:887px;width:295px;height:4px;background:var(--rule)}
.rule-v{position:absolute;left:862px;top:1248px;width:1px;height:42px;background:var(--rule)}

/* footer */
.site-footer{position:absolute;left:0;top:1290px;width:1300px;height:126px;background:var(--blue);color:var(--white)}
.foot-links{position:absolute;left:137px;top:43px;font-size:13px;display:flex;gap:18px}
.socials{position:absolute;left:139px;top:83px;display:flex;gap:10px}
.socials span{width:20px;height:20px;border-radius:50%;background:var(--white)}
.foot-brand{position:absolute;left:950px;top:35px;display:flex;align-items:center;gap:6px}
.foot-brand .brand-dot{width:35px;height:35px;background:var(--white)}
.foot-brand .brand-name{font-size:24px;line-height:24px}
.foot-brand .brand-tag{font-size:9.5px;line-height:11px}
.copy{position:absolute;left:965px;top:88px;font-size:14px}
.copy b{font-weight:700}
</style>
</head>
<body>
<div class="stage">

<svg width="0" height="0" style="position:absolute">
  <defs>
    <g id="tick"><rect x="1" y="1" width="13" height="13" rx="2" fill="none" stroke="#444" stroke-width="1.6"/><path d="M4 7.5l3 3 7-8" fill="none" stroke="#444" stroke-width="2"/></g>
    <g id="folder"><path d="M0 2h6l2 2h9v11H0z" fill="#777"/></g>
    <g id="doc"><rect x="1" y="1" width="13" height="15" fill="none" stroke="#888" stroke-width="1.2"/><path d="M4 5h7M4 8h7M4 11h5" stroke="#888" stroke-width="1.2"/></g>
  </defs>
</svg>

<header class="site-header">
  <div class="brand">
    <span class="brand-dot"></span>
    <div><div class="brand-name">skillnook</div><div class="brand-tag">A Knowledge Base PressLoom Theme</div></div>
  </div>
  <nav class="nav">
    <a class="active" href="#">HOME</a>
    <a style="left:885px" href="#">FAQ'S</a>
    <a style="left:950px" href="#">SHORTCODES</a>
    <a style="left:1058px" href="#">BLOG</a>
    <a style="left:1105px" href="#">CONTACT</a>
  </nav>
</header>

<section class="search-band">
  <div class="search-box">
    <span class="search-text">Have a question? Ask or enter a search term.</span>
    <span class="search-btn"><svg width="14" height="14" viewBox="0 0 14 14"><circle cx="6" cy="6" r="4.5" fill="none" stroke="#0585ab" stroke-width="2"/><path d="M9.5 9.5l3.5 3.5" stroke="#0585ab" stroke-width="2.2"/></svg>SEARCH</span>
  </div>
</section>

<main class="content"></main>

<h1 class="section-title"><span class="lead">Article</span> Categories</h1>

<article class="card tinted" style="left:147px;top:356px">
  <div class="card-icon filled" role="img" aria-label="Content SEO icon">
    <svg width="56" height="56" viewBox="0 0 56 56"><path d="M17 14h15l6 6v22H17z" fill="none" stroke="#fff" stroke-width="2"/><path d="M21 24h12M21 29h12M21 34h8" stroke="#fff" stroke-width="2"/><path d="M33 40l2-6 9-9 3 3-9 9z" fill="#fff"/></svg>
  </div>
  <h2 class="card-title">Content SEO</h2>
  <ul>
    <li><svg width="16" height="16"><use href="#tick"/></svg>Lorem Ipsum is simply dummy text .</li>
    <li><svg width="16" height="16"><use href="#tick"/></svg>It has survived not only five centuries.</li>
    <li><svg width="16" height="16"><use href="#tick"/></svg>The point of using Lorem Ipsum.</li>
    <li><svg width="16" height="16"><use href="#tick"/></svg>ManyLorem Ipsum is simply dummy.</li>
    <li><svg width="16" height="16"><use href="#tick"/></svg>text . desktop publishing packages.</li>
  </ul>
</article>

<article class="card" style="left:518px;top:356px">
  <div class="card-icon" role="img" aria-label="Technical SEO chart board icon">
    <svg width="56" height="56" viewBox="0 0 56 56"><rect x="13" y="15" width="30" height="21" fill="none" stroke="#4a5a1e" stroke-width="2.5"/><path d="M18 31l6-7 5 4 8-9" fill="none" stroke="#0585ab" stroke-width="2.2"/><path d="M28 36v6M22 43l6-7 6 7" fill="none" stroke="#4a5a1e" stroke-width="2"/></svg>
  </div>
  <h2 class="card-title">Technical SEO</h2>
  <ul>
    <li><svg width="16" height="16"><use href="#tick"/></svg>Lorem Ipsum is simply dummy text .</li>
    <li><svg width="16" height="16"><use href="#tick"/></svg>It has survived not only five centuries.</li>
    <li><svg width="16" height="16"><use href="#tick"/></svg>The point of using Lorem Ipsum.</li>
    <li><svg width="16" height="16"><use href="#tick"/></svg>ManyLorem Ipsum is simply dummy.</li>
    <li><svg width="16" height="16"><use href="#tick"/></svg>text . desktop publishing packages.</li>
  </ul>
</article>

<div class="divider" style="top:628px"></div>

<article class="card" style="left:147px;top:664px">
  <div class="card-icon" role="img" aria-label="Link building chain icon">
    <svg width="56" height="56" viewBox="0 0 56 56"><rect x="11" y="25" width="20" height="11" rx="5.5" transform="rotate(-40 21 30)" fill="none" stroke="#2c3e50" stroke-width="2.4"/><rect x="24" y="20" width="20" height="11" rx="5.5" transform="rotate(-40 34 25)" fill="none" stroke="#0585ab" stroke-width="2.4"/></svg>
  </div>
  <h2 class="card-title">Link Building</h2>
  <ul>
    <li><svg width="16" height="16"><use href="#tick"/></svg>Lorem Ipsum is simply dummy text .</li>
    <li class="no-tick"><svg width="16" height="16"><use href="#tick"/></svg>It has survived not only five centuries.</li>
    <li><svg width="16" height="16"><use href="#tick"/></svg>The point of using Lorem Ipsum.</li>
    <li><svg width="16" height="16"><use href="#tick"/></svg>ManyLorem Ipsum is simply dummy.</li>
    <li><svg width="16" height="16"><use href="#tick"/></svg>text . desktop publishing packages.</li>
  </ul>
</article>

<article class="card" style="left:518px;top:664px">
  <div class="card-icon" role="img" aria-label="Influencer marketing magnifier icon">
    <svg width="56" height="56" viewBox="0 0 56 56"><circle cx="25" cy="25" r="10" fill="none" stroke="#0585ab" stroke-width="3"/><path d="M32 32l10 10" stroke="#2c3e50" stroke-width="4" stroke-linecap="round"/></svg>
  </div>
  <h2 class="card-title">Influencer Marketing</h2>
  <ul>
    <li><svg width="16" height="16"><use href="#tick"/></svg>Lorem Ipsum is simply dummy text .</li>
    <li><svg width="16" height="16"><use href="#tick"/></svg>It has survived not only five centuries.</li>
    <li><svg width="16" height="16"><use href="#tick"/></svg>The point of using Lorem Ipsum.</li>
    <li><svg width="16" height="16"><use href="#tick"/></svg>ManyLorem Ipsum is simply dummy.</li>
    <li class="no-tick"><svg width="16" height="16"><use href="#tick"/></svg>text . desktop publishing packages.</li>
  </ul>
</article>

<div class="divider" style="top:940px"></div>

<article class="card" style="left:147px;top:975px">
  <div class="card-icon" role="img" aria-label="Paid marketing coin and pointer icon">
    <svg width="56" height="56" viewBox="0 0 56 56"><circle cx="25" cy="25" r="12" fill="none" stroke="#0585ab" stroke-width="2.4"/><circle cx="25" cy="25" r="7.5" fill="none" stroke="#0585ab" stroke-width="1.6"/><path d="M28 22c-1-1.5-6-1.5-6 1s6 1 6 3.5-5 2.5-6 1M25 19v12" fill="none" stroke="#0585ab" stroke-width="1.5"/><path d="M31 30l0 14 4-4 3 6 3-1.5-3-6h5z" fill="#2c3e50"/></svg>
  </div>
  <h2 class="card-title">Paid Marketing</h2>
  <ul>
    <li><svg width="16" height="16"><use href="#tick"/></svg>Lorem Ipsum is simply dummy text .</li>
    <li><svg width="16" height="16"><use href="#tick"/></svg>It has survived not only five centuries.</li>
    <li class="no-tick"><svg width="16" height="16"><use href="#tick"/></svg>The point of using Lorem Ipsum.</li>
    <li><svg width="16" height="16"><use href="#tick"/></svg>ManyLorem Ipsum is simply dummy.</li>
    <li><svg width="16" height="16"><use href="#tick"/></svg>text . desktop publishing packages.</li>
  </ul>
</article>

<article class="card" style="left:518px;top:975px">
  <div class="card-icon" role="img" aria-label="Analytics monitor icon">
    <svg width="56" height="56" viewBox="0 0 56 56"><rect x="11" y="15" width="34" height="22" rx="2" fill="none" stroke="#222" stroke-width="2.5"/><path d="M17 32v-5M22 32v-8M27 32v-6M32 32v-10M37 32v-7" stroke="#0585ab" stroke-width="3"/><path d="M24 37v4h8v-4M21 42h14" fill="none" stroke="#222" stroke-width="2.2"/></svg>
  </div>
  <h2 class="card-title">Analytics &amp; Measurement</h2>
  <ul>
    <li><svg width="16" height="16"><use href="#tick"/></svg>Lorem Ipsum is simply dummy text .</li>
    <li><svg width="16" height="16"><use href="#tick"/></svg>It has survived not only five centuries.</li>
    <li class="no-tick"><svg width="16" height="16"><use href="#tick"/></svg>The point of using Lorem Ipsum.</li>
    <li class="no-tick"><svg width="16" height="16"><use href="#tick"/></svg>ManyLorem Ipsum is simply dummy.</li>
    <li><svg width="16" height="16"><use href="#tick"/></svg>text . desktop publishing packages.</li>
  </ul>
</article>

<!-- sidebar: latest, popular, categories -->
<h3 class="widget-head" style="top:255px"><svg width="18" height="20" viewBox="0 0 18 20"><rect x="1" y="1" width="14" height="18" fill="none" stroke="#fff" stroke-width="2"/><path d="M4 6h8M4 10h8M4 14h8" stroke="#fff" stroke-width="1.6"/></svg>Latest Articles</h3>
<ul class="side-list" style="top:312px">
  <li style="height:37px"><svg width="16" height="17"><use href="#doc"/></svg>Customizing The Theme Colors</li>
  <li style="height:37px"><svg width="16" height="17"><use href="#doc"/></svg>Recommended Plugins</li>
  <li style="height:59px"><svg width="16" height="17"><use href="#doc"/></svg>Modifying The Background Image &amp;<br>Color</li>
  <li style="height:37px"><svg width="16" height="17"><use href="#doc"/></svg>Chaning The Skillnook Header</li>
</ul>
<div class="side-rule" style="top:500px"></div>

<h3 class="widget-head" style="top:525px"><svg width="20" height="20" viewBox="0 0 20 20"><rect x="1" y="3" width="15" height="15" fill="none" stroke="#fff" stroke-width="2"/><path d="M7 13l1-4 9-8 3 3-9 8z" fill="#fff"/></svg>Popular Articles</h3>
<ul class="side-list" style="top:582px">
  <li style="height:37px"><svg width="16" height="17"><use href="#doc"/></svg>How Secure Is My Password?</li>
  <li style="height:37px"><svg width="16" height="17"><use href="#doc"/></svg>What Technologies Are Used?</li>
  <li style="height:37px"><svg width="16" height="17"><use href="#doc"/></svg>How Do I Change My Password?</li>
  <li style="height:37px"><svg width="16" height="17"><use href="#doc"/></svg>Can I Change My Username?</li>
</ul>
<div class="side-rule" style="top:748px"></div>

<h3 class="widget-head" style="top:773px"><svg width="20" height="18" viewBox="0 0 20 18"><path d="M8 2H2v14h6" fill="none" stroke="#fff" stroke-width="2"/><path d="M7 9h9M12 4l5 5-5 5" fill="none" stroke="#fff" stroke-width="2.2"/></svg>Featured Categories</h3>
<ul class="side-list" style="top:832px">
  <li style="height:30px"><svg width="18" height="16"><use href="#folder"/></svg>Content SEO<span class="count">(6)</span></li>
  <li style="height:30px"><svg width="18" height="16"><use href="#folder"/></svg>Technical SEO<span class="count">(3)</span></li>
  <li style="height:30px"><svg width="18" height="16"><use href="#folder"/></svg>Link Building<span class="count">(9)</span></li>
  <li style="height:30px"><svg width="18" height="16"><use href="#folder"/></svg>Influencer Marketing<span class="count">(6)</span></li>
  <li style="height:30px"><svg width="18" height="16"><use href="#folder"/></svg>Paid Marketing<span class="count">(5)</span></li>
  <li style="height:30px"><svg width="18" height="16"><use href="#folder"/></svg>Analytics &amp; Measurement<span class="count">(2)</span></li>
</ul>

<div class="rule-v"></div>

<footer class="site-footer">
  <nav class="foot-links"><span>Home</span><span>|</span><span>FAQs</span><span>|</span><span>Shortcodes</span><span>|</span><span>Contact</span></nav>
  <div class="socials"><span></span><span></span><span></span><span></span></div>
  <div class="foot-brand">
    <span class="brand-dot"></span>
    <div><div class="brand-name">skillnook</div><div class="brand-tag">A Knowledge Base PressLoom Theme</div></div>
  </div>
  <p class="copy">© Copyright, 2017, <b>skillnook</b></p>
</footer>

</div>
</body>
</html>
```